Plurabel TV needs a van wrap Design and logo

Morland Cargon Wrap Design ( partial wrap or 3/4 full wrap ).. I need a logo too...

I'd will really like if someone can wrap the cargon similar to the qdv within the files.

Target Market(s)

Home Owners

Logo Text

Plurabel TV Installers

Font styles to use
Sans Serif

Colors
ec1f27

Requirements
Must have
• My info 586-214-9073, www.plurabeltv.com, My colors are red white and black .. i will like the best of the best seal as in my old design as outlined with spec below..
• I'm ready to have the wrap installed like asap
Nice to have
• LOGO

```html
<!DOCTYPE html>
<html lang="en">
<head>
<meta charset="utf-8">
<title>Plurabel TV Installers – Van Wrap</title>
<link rel="stylesheet" href="https://fonts.googleapis.com/css2?family=Roboto+Condensed:wght@400;700;900&display=swap">
<style>
  :root {
    --brand-red: #ec1f27;
    --wrap-black: #151515;
    --wrap-white: #ffffff;
    --body-grey: #f2f2f2;
    --glass: #5b5f63;
    --tyre: #1c1c1c;
    --hub: #a9adb1;
    --room-light: #cdbba3;
    --room-dark: #6b5a4b;
    --ink: #111111;
  }
  html, body {
    margin: 0;
    width: 1200px;
    height: 1000px;
    overflow: hidden;
    background: #ffffff;
  }
  .wrap-sheet { display: block; width: 1200px; height: 1000px; }
  .brand-name { font-family: "Roboto Condensed", sans-serif; font-weight: 900; fill: var(--wrap-white); }
  .tagline { font-family: "Roboto Condensed", sans-serif; font-weight: 700; font-size: 17px; fill: var(--wrap-white); }
  .phone { font-family: "Roboto Condensed", sans-serif; font-weight: 700; font-size: 34px; fill: var(--ink); }
  .web { font-family: "Roboto Condensed", sans-serif; font-weight: 400; font-size: 15px; fill: var(--ink); }
  .service-strip-text { font-family: "Roboto Condensed", sans-serif; font-weight: 700; font-size: 14px; fill: var(--wrap-white); letter-spacing: .3px; }
</style>
</head>
<body>
<svg class="wrap-sheet" viewBox="0 0 1200 1000" xmlns="http://www.w3.org/2000/svg">
  <defs>
    <linearGradient id="room-tone" x1="0" y1="0" x2="1" y2="1">
      <stop offset="0" stop-color="var(--room-dark)"/>
      <stop offset=".55" stop-color="var(--room-light)"/>
      <stop offset="1" stop-color="#b0413a"/>
    </linearGradient>
    <clipPath id="van-body-clip">
      <path d="M45,395 L45,300 Q55,252 120,228 L180,195 Q232,62 300,48 L1120,40 Q1152,42 1154,80 L1160,380 L1150,398 Z"/>
    </clipPath>
    <g id="van-art">
      <g clip-path="url(#van-body-clip)">
        <rect class="body-panel" x="0" y="0" width="1200" height="420" fill="var(--body-grey)"/>
        <path class="rear-swoop" d="M590,300 Q690,120 900,40 L1170,35 L1170,300 Z" fill="var(--brand-red)"/>
        <path class="swoop-line-black" d="M575,302 Q675,118 885,38" fill="none" stroke="var(--wrap-black)" stroke-width="14"/>
        <path class="swoop-line-white" d="M592,302 Q692,122 902,40" fill="none" stroke="var(--wrap-white)" stroke-width="6"/>
        <path class="room-scene" role="img" aria-label="Photo of a living room with a wall-mounted flat-screen TV" d="M640,292 Q700,205 790,190 L1110,190 L1110,258 Z" fill="url(#room-tone)"/>
        <path class="lower-band" d="M0,330 L330,318 L1170,272 L1170,420 L0,420 Z" fill="var(--wrap-black)"/>
        <path class="accent-stripe" d="M350,314 L1170,266 L1170,290 L720,302 Z" fill="var(--brand-red)"/>
        <path class="accent-line" d="M330,318 L1170,258" fill="none" stroke="var(--wrap-white)" stroke-width="4"/>
        <rect class="service-strip" x="330" y="360" width="480" height="28" fill="var(--brand-red)"/>
      </g>
      <path class="windscreen" d="M190,190 Q240,75 290,62 L300,190 Z" fill="var(--glass)"/>
      <path class="cab-window" d="M315,62 L470,60 L470,200 L315,200 Z" fill="var(--glass)"/>
      <path class="headlamp" d="M58,250 Q90,232 140,226 L132,262 Q90,270 58,270 Z" fill="#d9dde0"/>
      <circle class="tyre" cx="225" cy="392" r="72" fill="var(--tyre)"/>
      <circle class="hub" cx="225" cy="392" r="44" fill="var(--hub)"/>
      <circle class="tyre" cx="915" cy="392" r="72" fill="var(--tyre)"/>
      <circle class="hub" cx="915" cy="392" r="44" fill="var(--hub)"/>
      <circle class="quality-seal" cx="735" cy="240" r="22" fill="var(--brand-red)"/>
    </g>
  </defs>

  <!-- driver side -->
  <g class="van van-left-side">
    <use href="#van-art"/>
    <text class="brand-name" x="880" y="102" font-size="56">Plurabel</text>
    <text class="brand-name" x="895" y="142" font-size="34">TV Installers</text>
    <text class="tagline" x="880" y="174">We Hang TV's &amp; Hide the Wires</text>
    <text class="phone" x="265" y="272">586-214-9073</text>
    <text class="web" x="278" y="292">www.PlurabelTV.com</text>
    <text class="service-strip-text" x="570" y="379" text-anchor="middle">PROFESSIONAL TV INSTALLER - HOME THEATERS - HD ANTENNA INSTALLER</text>
  </g>

  <!-- passenger side -->
  <g class="van van-right-side">
    <use href="#van-art" transform="translate(1200,500) scale(-1,1)"/>
    <text class="brand-name" x="85" y="602" font-size="56">Plurabel</text>
    <text class="brand-name" x="100" y="642" font-size="34">TV Installers</text>
    <text class="tagline" x="88" y="674">We Hang TV's &amp; Hide the Wires</text>
    <text class="phone" x="745" y="772">586-214-9073</text>
    <text class="web" x="758" y="792">www.PlurabelTV.com</text>
    <text class="service-strip-text" x="630" y="879" text-anchor="middle">PROFESSIONAL TV INSTALLER - HOME THEATERS - HD ANTENNA INSTALLER</text>
  </g>
</svg>
</body>
</html>
```